New Business Card Design Project

hello again,
i have an awful year and we were not able to complete our logo plan. we would like to use our #1 logo for business card design process. the primary colors for business card should be white background with orange & black letters. our business is mobil truck cranes. we deliver heavy stuff and unload cargo with crane that is mounted on our trucks.
here is our business card info:
HARBORLINE LIFT HAULERS, INC.
482 WICKHAM AVE
BRIARWOOD, CT 06905
OFFICE - 555 430 2291
DIRECT - 1 888 LIFT HAULS
GERALD@HLHAUL.EXAMPLE
PLEASE also try to get our slogan on card .... "Our Loads Keep Climbin"
lastly please also put "24 hour Knuckleboom Service"
you can call me anytime 24/7 to discuss...my cell # is: 555 907 4463
please also list: Gerald Pruitt, President
Target Market(s)
Heavy Construction industry
Industry/Entity Type
heavy construction industry
Contact Information for Business Card
24 Hr Knuckleboom Service

```html
<!DOCTYPE html>
<html lang="en">
<head>
<meta charset="utf-8">
<title>Harborline Lift Haulers – Business Card</title>
<link rel="stylesheet" href="https://fonts.googleapis.com/css2?family=Arimo:wght@400;700&display=swap">
<style>
  :root {
    --orange: #e8730c;
    --orange-deep: #c85f05;
    --ink: #1f1f1f;
    --charcoal: #2b2b2b;
    --paper: #ffffff;
    --stage: #ebebea;
    --rule: #3a3a3a;
    --light: #f2f2f2;
  }
  * { margin: 0; padding: 0; box-sizing: border-box; }
  html, body { width: 1200px; height: 801px; overflow: hidden; }
  body {
    background: var(--stage);
    font-family: "Arimo", Arial, sans-serif;
    display: flex;
    align-items: center;
    justify-content: center;
    gap: 40px;
  }
  .card {
    width: 540px;
    height: 309px;
    position: relative;
    border-bottom: 3px solid var(--orange-deep);
    box-shadow: 0 10px 24px rgba(0,0,0,0.18);
  }

  /* Front */
  .card-front { background: var(--paper); color: var(--ink); display: flex; }
  .front-brand {
    width: 262px;
    display: flex;
    align-items: center;
    justify-content: center;
    gap: 10px;
    padding: 0 18px;
  }
  .brand-mark { width: 14px; height: 14px; background: var(--orange); flex: none; }
  .brand-name {
    font-weight: 700;
    font-size: 19px;
    line-height: 1.2;
    color: var(--ink);
  }
  .front-divider {
    width: 1px;
    background: var(--rule);
    margin: 64px 0 58px;
  }
  .front-details { padding: 62px 0 0 22px; font-size: 12.5px; line-height: 1.35; }
  .person-name { color: var(--orange); font-weight: 700; font-size: 17px; letter-spacing: 0.3px; }
  .person-title { font-size: 13px; margin-bottom: 12px; }
  .address { margin-bottom: 12px; }
  .contact-line { display: flex; align-items: center; gap: 7px; }
  .contact-line svg { width: 11px; height: 11px; flex: none; }

  /* Back */
  .card-back {
    background: linear-gradient(160deg, #333 0%, var(--charcoal) 55%, #222 100%);
    color: var(--light);
    text-align: center;
  }
  .back-brand {
    position: absolute;
    top: 56px; left: 0; right: 0;
    display: flex;
    justify-content: center;
    align-items: center;
    gap: 10px;
  }
  .back-brand .brand-name { color: var(--paper); font-size: 24px; }
  .slogan { position: absolute; top: 168px; left: 0; right: 0; font-size: 14px; }
  .service-band {
    position: absolute;
    top: 192px; left: 60px; right: 60px;
    height: 30px;
    background: linear-gradient(90deg, rgba(200,95,5,0) 0%, var(--orange-deep) 35%, var(--orange-deep) 65%, rgba(200,95,5,0) 100%);
    font-size: 17px;
    line-height: 30px;
    color: var(--paper);
  }
  .cell-line {
    position: absolute;
    top: 246px; left: 0; right: 0;
    font-size: 14px;
    font-weight: 700;
  }
  .cell-number { color: var(--orange); font-size: 17px; margin-left: 6px; }
</style>
</head>
<body>
  <section class="card card-front">
    <div class="front-brand">
      <span class="brand-mark"></span>
      <span class="brand-name">HARBORLINE LIFT HAULERS, INC.</span>
    </div>
    <div class="front-divider"></div>
    <div class="front-details">
      <p class="person-name">GERALD PRUITT</p>
      <p class="person-title">President</p>
      <p class="address">482 WICKHAM AVE<br>BRIARWOOD, CT 06905</p>
      <p class="contact-line">
        <svg viewBox="0 0 12 12" aria-hidden="true"><path d="M2.5 1 L4.5 1 L5.2 3.6 L3.9 4.6 Q5 7 7.4 8.1 L8.4 6.8 L11 7.5 L11 9.5 Q11 11 9.3 11 Q1 10 1 2.7 Q1 1 2.5 1 Z" fill="var(--orange)"/></svg>
        555 430 2291
      </p>
      <p class="contact-line">
        <svg viewBox="0 0 12 12" aria-hidden="true"><rect x="3" y="0.8" width="6" height="10.4" rx="1" fill="none" stroke="var(--orange)" stroke-width="1.2"/><circle cx="6" cy="9.4" r="0.6" fill="var(--orange)"/></svg>
        1 888 LIFT HAULS
      </p>
      <p class="contact-line">
        <svg viewBox="0 0 12 12" aria-hidden="true"><rect x="0.8" y="2.3" width="10.4" height="7.4" fill="none" stroke="var(--orange)" stroke-width="1.2"/><path d="M0.8 2.5 L6 6.6 L11.2 2.5" fill="none" stroke="var(--orange)" stroke-width="1.2"/></svg>
        GERALD@HLHAUL.EXAMPLE
      </p>
    </div>
  </section>

  <section class="card card-back">
    <div class="back-brand">
      <span class="brand-mark"></span>
      <span class="brand-name">HARBORLINE LIFT HAULERS, INC.</span>
    </div>
    <p class="slogan">Our Loads Keep Climbin</p>
    <p class="service-band">24 hour Knuckleboom Service</p>
    <p class="cell-line">you can call me anytime 24/7 to discuss...my cell<span class="cell-number">555 907 4463</span></p>
  </section>
</body>
</html>
```